Out of town New Masters of Accounting

size of ad is 7” x 9.6”
please leave one inch on bottom for footer
We want to attract out of town students to join this master's in accounting program.
You DO NOT  have to use a picture of a person.
But if you do, it should be a  male with a white shirt and should not have long hair.(look like a young executive)
THE TEXT OF THE AD IS IN THE ATTACHMENTS
THE CAP LETTERS ARE THE INSTRUCTIONS

The age we are trying to attract is from 20-30 of ages.
- a clear ad .. the text should not take up the entire ad.. it should not be very crowded -
it should be an attractive ad that people would want to see and stand out
- the text very big and take up the entire ad

```html
<!DOCTYPE html>
<html lang="en">
<head>
<meta charset="utf-8">
<title>Remote Masters of Science in Accounting</title>
<link href="https://fonts.googleapis.com/css2?family=Heebo:wght@100;200;300;400;500;700;800;900&family=Oswald:wght@500&display=swap" rel="stylesheet">
<style>
  :root {
    --header-grey: #9d9d9f;
    --band-grey: #c9c9c9;
    --band-line: #a3a3a3;
    --dark-grey: #5f5f61;
    --orange: #f68b1f;
    --orange-light: #f8a04c;
    --orange-deep: #e16a26;
    --ink: #111111;
    --ink-soft: #3b3b3d;
    --white: #ffffff;
    --triangle: #d3d3d5;
    --seal-gold: #f9c23c;
    --seal-dark: #2f2f31;
    --shirt: #eef1f4;
    --laptop: #77787c;
    --tie-blue: #9fb9cf;
    --desk: #dfe7ea;
  }
  * { margin: 0; padding: 0; box-sizing: border-box; }
  html, body { width: 848px; height: 1200px; overflow: hidden; background: var(--white); }
  body { font-family: "Heebo", Arial, sans-serif; color: var(--ink); }
  .ad { position: relative; width: 848px; height: 1200px; overflow: hidden; background: var(--white); }

  .header { position: absolute; left: 0; top: 0; width: 848px; height: 228px; background: var(--header-grey); }
  .header-stripe { position: absolute; left: 0; top: 228px; width: 848px; height: 10px;
    background: linear-gradient(90deg, var(--orange-light), var(--orange) 60%, var(--orange-deep)); }
  .header-text { position: absolute; right: 53px; top: 88px; text-align: right; }
  .header-kicker { font-weight: 800; font-size: 32px; color: var(--white); line-height: 1; }
  .header-title { font-weight: 200; font-size: 42px; color: var(--white); line-height: 1; margin-top: 12px; letter-spacing: -0.6px; }
  .header-sub { font-weight: 700; font-size: 20px; color: #4a4a4c; margin-top: 12px; line-height: 1; }

  .hero-photo { position: absolute; left: 0; top: 238px; width: 848px; height: 452px;
    background:
      linear-gradient(90deg, #ffffff 0%, rgba(255,255,255,0.95) 24%, rgba(255,255,255,0) 58%),
      radial-gradient(ellipse 120px 200px at 730px 200px, rgba(159,185,207,0.55), rgba(159,185,207,0) 100%),
      radial-gradient(ellipse 170px 150px at 820px 300px, rgba(119,120,124,0.75), rgba(119,120,124,0) 100%),
      radial-gradient(ellipse 260px 260px at 690px 160px, var(--shirt), rgba(238,241,244,0) 100%),
      linear-gradient(180deg, #f6f8fa 0%, #eceff2 55%, var(--desk) 78%, #e8eef0 100%); }

  .headline { position: absolute; left: 50px; top: 310px; }
  .headline-lead { font-weight: 700; font-size: 20.5px; color: var(--orange); line-height: 1; }
  .headline-degree { font-weight: 800; font-size: 35px; line-height: 1; margin-top: 22px; letter-spacing: -0.2px; }
  .headline-degree .in { font-weight: 400; font-size: 23px; }
  .headline-field { font-weight: 100; font-size: 72px; line-height: 1; margin-top: 10px; letter-spacing: 0; margin-left: -3px; }

  .band { position: absolute; left: 0; top: 690px; width: 848px; height: 26px; background: var(--band-grey);
    border-top: 5px solid var(--band-line); }

  .start-date { position: absolute; left: 602px; top: 638px; width: 246px; }
  .start-date-main { height: 97px; background: linear-gradient(90deg, var(--orange-light), var(--orange) 60%, var(--orange-deep));
    border-top-left-radius: 10px; position: relative; overflow: hidden; }
  .start-date-label { position: absolute; left: 25px; top: 10px; font-weight: 700; font-size: 17px; color: var(--white); line-height: 1.2; }
  .start-date-month { position: absolute; left: 25px; top: 33px; font-weight: 900; font-size: 34px; color: var(--white); line-height: 1; letter-spacing: 0.5px; }
  .start-date-day { position: absolute; left: 146px; top: 12px; font-weight: 100; font-size: 92px; color: var(--white); line-height: 1; letter-spacing: 2px; }
  .start-date-note { height: 39px; background: var(--dark-grey); border-bottom-left-radius: 10px;
    padding-left: 25px; font-weight: 800; font-size: 22px; color: var(--white); line-height: 39px; }

  .ranking { position: absolute; left: 70px; top: 742px; display: flex; align-items: center; }
  .ranking-mark { width: 148px; height: 128px; }
  .ranking-name { margin-left: 21px; font-weight: 800; font-size: 20px; color: var(--orange); line-height: 1.1; }

  .accolade { position: absolute; left: 70px; top: 899px; font-weight: 500; font-size: 17px; line-height: 19px; color: var(--ink); }

  .placement { position: absolute; left: 70px; top: 986px; width: 332px; height: 149px;
    border: 1px solid var(--orange); border-radius: 10px; overflow: hidden; }
  .placement-head { background: var(--orange); height: 55px; padding: 8px 0 0 20px; color: var(--white); line-height: 21px; }
  .placement-org { font-weight: 400; font-size: 16px; }
  .placement-title { font-weight: 700; font-size: 16px; }
  .placement-list { list-style: none; padding: 7px 0 0 18px; }
  .placement-list li { font-weight: 400; font-size: 15px; color: var(--ink-soft); line-height: 28px; position: relative; padding-left: 14px; }
  .placement-list li::before { content: ""; position: absolute; left: 0; top: 12px; width: 6px; height: 6px; border-radius: 50%; background: var(--orange); }

  .corner { position: absolute; right: 0; bottom: 0; width: 190px; height: 190px; }
  .seal { position: absolute; left: 688px; top: 1037px; width: 130px; height: 130px; }
  .seal-text { font-family: "Oswald", "Heebo", sans-serif; font-weight: 500; fill: var(--white); }
</style>
</head>
<body>
<main class="ad">
  <header class="header">
    <div class="header-text">
      <p class="header-kicker">All New!</p>
      <p class="header-title">REMOTE PROGRAM</p>
      <p class="header-sub">For out of Town Students</p>
    </div>
  </header>
  <div class="header-stripe"></div>

  <div class="hero-photo" role="img" aria-label="Young executive in a white shirt and striped blue tie with hands clasped, seated at a desk with a laptop, an alarm clock and printed charts"></div>

  <section class="headline">
    <p class="headline-lead">Advance further in your career with a</p>
    <h1 class="headline-degree">Masters of Science <span class="in">in</span></h1>
    <p class="headline-field">ACCOUNTING</p>
  </section>

  <div class="band"></div>

  <aside class="start-date">
    <div class="start-date-main">
      <span class="start-date-label">Beginning</span>
      <span class="start-date-month">AUGUST</span>
      <span class="start-date-day">17</span>
    </div>
    <div class="start-date-note">New lower prices</div>
  </aside>

  <section class="ranking">
    <svg class="ranking-mark" viewBox="0 0 148 128" aria-hidden="true">
      <circle cx="74" cy="66" r="48" fill="var(--orange)"/>
    </svg>
    <p class="ranking-name">Graduvista<br>Ranking 2019</p>
  </section>

  <p class="accolade">Graduvista -- Northfield Crest University (NCU)<br>Master in Accounting Program Received<br>The Highest possible star rating</p>

  <section class="placement">
    <div class="placement-head">
      <p class="placement-org">CareerBridge Alliance</p>
      <p class="placement-title">Job Placement Advantage</p>
    </div>
    <ul class="placement-list">
      <li>96% placement rate</li>
      <li>8 placement coordinators</li>
      <li>Decades of relationships with 100’s of firm</li>
    </ul>
  </section>

  <svg class="corner" viewBox="0 0 190 190" aria-hidden="true">
    <polygon points="190,0 190,190 0,190" fill="var(--triangle)"/>
  </svg>

  <svg class="seal" viewBox="0 0 132 132" role="img" aria-label="A master in only 15 months">
    <defs>
      <path id="seal-arc" d="M24,66 A42,42 0 0 1 108,66"/>
    </defs>
    <circle cx="66" cy="66" r="64" fill="var(--seal-gold)"/>
    <circle cx="66" cy="66" r="55" fill="var(--seal-dark)"/>
    <text class="seal-text" font-size="11" letter-spacing="1"><textPath href="#seal-arc" startOffset="50%" text-anchor="middle">A MASTER IN ONLY</textPath></text>
    <text class="seal-text" x="66" y="82" font-size="36" text-anchor="middle">15</text>
    <line x1="38" y1="88" x2="94" y2="88" stroke="var(--white)" stroke-width="0.8" stroke-dasharray="1.5 2"/>
    <text class="seal-text" x="66" y="103" font-size="11" text-anchor="middle">MONTHS</text>
  </svg>
</main>
</body>
</html>
```